Zielgruppe
Wir betreiben eine Bäckerei mit Kaffeehaus als Nahversorger in A-3032 Lindenau. Das design soll natürlich unsere Kunden ansprechen.
Aufgabenstellung
Es wird ein neuer Schriftzug horizontal für das Sanierungsobjekt gesucht. Folgende Vorgaben sind wünschenswert:
Schriftzug - Außenbeschilderung;
Schriftzug -Cafe- linksbündig, Schriftzug -Kleffinger- mittig, Schriftzug -Bäckerei- rechstbündig. Die Außenbeschilderung soll ca. 5m lang und ca. 70cm hoch sein. Siehe auch Bestandsobjekt im Anhang. Vorraussetzung ist, das das Design auf ALU oder Plexiglas folierbar ist.
Familienwappen;
Eine Druckversion ist im Anhang ersichtlich, eine vereinfachte Darstellung wäre durchaus möglich durch etwa Konturen/ Linien etc..
Farben;
Am Foto ersichtlich die neue Farbe der Fassade links und rechts.
Banner für zwischen den Fenstern - vertikal;
1x Design für Bäckerei (Semmel/ Brötchen, Korb mit Gebäck, etc.), Schriftzug oben -Bäckerei-, Schriftzug unten -Kleffinger-.
1x Design für Cafe (Kaffeetasse, Cupcake, etc), Schriftzug oben -Cafe-, Schriftzug unten -Kleffinger-.
Designvorschlag; helle Schrift auf dunklem Hintergrund- weinrot, smaragtgrün, dunkelblau???
Natürlich sind auch alternative/ abweichende Vorschläge wünschenswert.
Wir freuen uns auf die Designs !!!

```html
<!DOCTYPE html>
<html lang="de">
<head>
<meta charset="utf-8">
<title>Cafe Kleffinger Bäckerei – Beschilderung</title>
<link rel="stylesheet" href="https://fonts.googleapis.com/css2?family=Cinzel:wght@400;600&family=Yesteryear&family=Open+Sans:wght@400;500&display=swap">
<style>
  :root {
    --green: #b7cc83;
    --green-soft: #dfe9c6;
    --green-pale: #f1f6e6;
    --ink: #4a4a4a;
    --grey: #5a5a5a;
    --paper: #ffffff;
  }
  * { margin: 0; padding: 0; box-sizing: border-box; }
  html, body { width: 1200px; height: 1200px; overflow: hidden; background: var(--paper); }
  .canvas { position: relative; width: 1200px; height: 1200px; }

  .frame { position: absolute; border: 10px solid var(--green); background: var(--paper); }
  .frame::after {
    content: ""; position: absolute; inset: 5px; border: 2px solid var(--green); pointer-events: none;
  }

  .script {
    font-family: "Yesteryear", cursive;
    font-weight: 400;
    color: var(--green);
    -webkit-text-stroke: 0.9px var(--ink);
    paint-order: stroke fill;
    line-height: 1;
    position: absolute;
    white-space: nowrap;
  }
  .wordmark {
    font-family: "Cinzel", serif;
    font-weight: 600;
    color: var(--green);
    -webkit-text-stroke: 1px var(--ink);
    line-height: 1;
    position: absolute;
    white-space: nowrap;
  }

  /* Fassadenschild */
  .facade-sign { left: 125px; top: 328px; width: 983px; height: 88px; border-width: 6px; }
  .facade-sign::after { inset: 5px; }
  .facade-sign .cafe { left: 80px; top: 12px; font-size: 60px; }
  .facade-sign .name { left: 240px; top: 20px; font-size: 50px; letter-spacing: 7px; }
  .facade-sign .baeckerei { left: 712px; top: 15px; font-size: 54px; }

  /* Banner */
  .banner { top: 447px; width: 258px; height: 561px; }
  .banner--baeckerei { left: 330px; }
  .banner--cafe { left: 617px; }
  .banner .title {
    left: 0; right: 0; text-align: center; font-weight: 400;
    text-shadow: 2px 3px 3px rgba(0,0,0,0.3);
  }
  .banner--baeckerei .title { top: 30px; font-size: 50px; }
  .banner--cafe .title { top: 22px; font-size: 62px; }

  .illustration {
    position: absolute; display: block;
    left: 14px; top: 150px; width: 210px; height: 170px;
  }

  .banner .brand {
    position: absolute; left: 0; right: 0; top: 342px; text-align: center;
    font-family: "Cinzel", serif; font-size: 19px; font-weight: 400; color: var(--grey);
  }
  .banner .tagline {
    position: absolute; left: 0; right: 0; top: 369px; text-align: center;
    font-family: "Open Sans", sans-serif; font-size: 10.5px; font-weight: 500;
    line-height: 14px; color: var(--grey); text-transform: uppercase;
  }
  .banner .crest { position: absolute; left: 76px; top: 402px; width: 86px; height: 98px; display: block; }
  .banner .crest-note {
    position: absolute; left: 0; right: 0; top: 509px; text-align: center;
    font-family: "Open Sans", sans-serif; font-size: 7px; color: var(--grey); text-transform: uppercase;
  }
</style>
</head>
<body>
<main class="canvas">

  <section class="frame facade-sign" aria-label="Fassadenschild">
    <span class="script cafe">Cafe</span>
    <span class="wordmark name">KLEFFINGER</span>
    <span class="script baeckerei">Bäckerei</span>
  </section>

  <section class="frame banner banner--baeckerei" aria-label="Banner Bäckerei">
    <h2 class="script title">Bäckerei</h2>
    <svg class="illustration" role="img" aria-label="Illustration: Bäckermütze, Brotlaib und Ähren" viewBox="0 0 210 170">
      <defs>
        <radialGradient id="glow-bread" cx="50%" cy="50%" r="50%">
          <stop offset="0%" stop-color="#dfe9c6"/>
          <stop offset="70%" stop-color="#eef4e0"/>
          <stop offset="100%" stop-color="#ffffff"/>
        </radialGradient>
      </defs>
      <ellipse cx="105" cy="85" rx="105" ry="85" fill="url(#glow-bread)"/>
    </svg>
    <p class="brand">KLEFFINGER</p>
    <p class="tagline">Die Bäckerei in<br>Lindenau</p>
    <svg class="crest" role="img" aria-label="Familienwappen" viewBox="0 0 86 98">
      <defs>
        <radialGradient id="glow-crest-a" cx="50%" cy="50%" r="50%">
          <stop offset="0%" stop-color="#d6e3b4"/>
          <stop offset="75%" stop-color="#e8f0d4"/>
          <stop offset="100%" stop-color="#ffffff"/>
        </radialGradient>
      </defs>
      <ellipse cx="43" cy="49" rx="43" ry="49" fill="url(#glow-crest-a)"/>
    </svg>
    <p class="crest-note">Familienwappen seit 1380</p>
  </section>

  <section class="frame banner banner--cafe" aria-label="Banner Cafe">
    <h2 class="script title">Cafe</h2>
    <svg class="illustration" role="img" aria-label="Illustration: dampfende Kaffeetasse auf Unterteller mit Ranken" viewBox="0 0 210 170">
      <defs>
        <radialGradient id="glow-cup" cx="50%" cy="50%" r="50%">
          <stop offset="0%" stop-color="#dfe9c6"/>
          <stop offset="70%" stop-color="#eef4e0"/>
          <stop offset="100%" stop-color="#ffffff"/>
        </radialGradient>
      </defs>
      <ellipse cx="105" cy="85" rx="105" ry="85" fill="url(#glow-cup)"/>
    </svg>
    <p class="brand">KLEFFINGER</p>
    <p class="tagline">Die Bäckerei in<br>Lindenau</p>
    <svg class="crest" role="img" aria-label="Familienwappen" viewBox="0 0 86 98">
      <defs>
        <radialGradient id="glow-crest-b" cx="50%" cy="50%" r="50%">
          <stop offset="0%" stop-color="#d6e3b4"/>
          <stop offset="75%" stop-color="#e8f0d4"/>
          <stop offset="100%" stop-color="#ffffff"/>
        </radialGradient>
      </defs>
      <ellipse cx="43" cy="49" rx="43" ry="49" fill="url(#glow-crest-b)"/>
    </svg>
    <p class="crest-note">Familienwappen seit 1380</p>
  </section>

</main>
</body>
</html>
```